Business Card Design

We need a business card design for a consulting firm which provides safety and risk management consulting services for public venues, hotels and tourist attractions. The business card design should include the attached logo unedited with a design based on incorporating the existing logo with a design of geometric patterns or lines on a predominantly white background.

Industry/Entity Type

Business

Contact Information for Business Card

Dane Morravik
Director & Principal Consultant

Ph: +61 (0) 478506 214
PO Box 456 Brenmoor Vale, NSW Australia 2611
info@corvalrisksafety.example

(back of card to include website www.corvalrisksafety.example

```html
<!DOCTYPE html>
<html lang="en">
<head>
<meta charset="utf-8">
<title>Corval Risk &amp; Safety — Business Card</title>
<link rel="stylesheet" href="https://fonts.googleapis.com/css2?family=Open+Sans:wght@400;600;700&display=swap">
<style>
  :root {
    --page: #e9eaeb;
    --card: #ffffff;
    --band-grey: #ebebeb;
    --brand-blue: #2196d8;
    --brand-green: #5cb63f;
    --ink: #1f1f1f;
    --muted: #3a3a3a;
  }
  * { box-sizing: border-box; margin: 0; padding: 0; }
  html, body {
    width: 1200px; height: 900px; overflow: hidden;
    background: var(--page);
    font-family: "Open Sans", Arial, sans-serif;
    color: var(--ink);
  }
  .stage {
    width: 1200px; height: 900px;
    display: flex; flex-direction: column; align-items: center; justify-content: center;
    gap: 50px;
  }
  .card {
    position: relative;
    width: 640px; height: 366px;
    background: var(--card);
    box-shadow: 0 6px 18px rgba(0,0,0,0.18);
    overflow: hidden;
  }
  .stripe-green {
    position: absolute; left: 0; right: 0; height: 8px; background: var(--brand-green);
  }
  .stripe-blue {
    position: absolute; left: 0; right: 0; bottom: 0; height: 40px; background: var(--brand-blue);
  }

  /* Back */
  .card-back .brand-mark {
    position: absolute; top: 110px; left: 0; right: 0;
    display: flex; align-items: center; justify-content: center; gap: 14px;
  }
  .brand-dot { width: 34px; height: 34px; border-radius: 50%; background: var(--brand-blue); }
  .brand-name {
    font-weight: 700; font-size: 34px; color: var(--brand-blue); letter-spacing: 0.5px;
  }
  .card-back .website {
    position: absolute; top: 256px; left: 0; right: 0; text-align: center;
    font-size: 17px; font-weight: 600; color: var(--ink);
  }
  .card-back .stripe-green { bottom: 40px; }

  /* Front */
  .card-front .holder {
    position: absolute; top: 50px; right: 36px; text-align: right;
  }
  .holder-name {
    font-size: 22px; font-weight: 700; color: var(--brand-blue); letter-spacing: 1px;
    text-transform: uppercase;
  }
  .holder-title { font-size: 16px; color: var(--muted); }
  .card-front .brand-mark {
    position: absolute; top: 138px; left: 34px;
    display: flex; align-items: center; gap: 10px;
  }
  .card-front .brand-dot { width: 26px; height: 26px; }
  .card-front .brand-name { font-size: 27px; }
  .contact-band {
    position: absolute; left: 0; right: 0; top: 196px; bottom: 48px;
    background: var(--band-grey);
  }
  .card-front .stripe-green { bottom: 40px; }
  .address {
    position: absolute; top: 214px; left: 34px;
    font-size: 15px; line-height: 1.35; color: var(--ink);
    display: flex; gap: 6px;
  }
  .contact-lines {
    position: absolute; top: 244px; left: 318px;
    font-size: 15px; line-height: 1.55; color: var(--ink);
  }
  .contact-line { display: flex; align-items: center; gap: 8px; }
  .icon { width: 13px; height: 13px; flex: none; fill: var(--brand-blue); }
</style>
</head>
<body>
<main class="stage">

  <section class="card card-back" aria-label="Card back">
    <div class="brand-mark">
      <span class="brand-dot"></span>
      <span class="brand-name">CORVAL RISK &amp; SAFETY</span>
    </div>
    <p class="website">www.corvalrisksafety.example</p>
    <div class="stripe-green"></div>
    <div class="stripe-blue"></div>
  </section>

  <section class="card card-front" aria-label="Card front">
    <div class="holder">
      <p class="holder-name">Dane Morravik</p>
      <p class="holder-title">Director &amp; Principal Consultant</p>
    </div>
    <div class="contact-band"></div>
    <div class="brand-mark">
      <span class="brand-dot"></span>
      <span class="brand-name">CORVAL RISK &amp; SAFETY</span>
    </div>
    <div class="address">
      <svg class="icon" viewBox="0 0 12 16" aria-hidden="true"><path d="M6 0a6 6 0 0 0-6 6c0 4.5 6 10 6 10s6-5.5 6-10a6 6 0 0 0-6-6zm0 8.5A2.5 2.5 0 1 1 6 3.5a2.5 2.5 0 0 1 0 5z"/></svg>
      <p>PO Box 456 Brenmoor Vale,<br>NSW Australia 2611</p>
    </div>
    <div class="contact-lines">
      <p class="contact-line">
        <svg class="icon" viewBox="0 0 16 16" aria-hidden="true"><path d="M3.6 1l2.3 3-1.4 1.7c.9 2 2.6 3.7 4.7 4.7l1.7-1.4 3 2.3-1.3 2.8C7 14 2 9 1 2.3z"/></svg>
        +61 (0) 478506 214
      </p>
      <p class="contact-line">
        <svg class="icon" viewBox="0 0 16 12" aria-hidden="true"><path d="M0 0h16v12H0z M1 1l7 5 7-5" fill="var(--brand-blue)"/><path d="M1 1.5l7 5 7-5" fill="none" stroke="#fff" stroke-width="1.2"/></svg>
        info@corvalrisksafety.example
      </p>
    </div>
    <div class="stripe-green"></div>
    <div class="stripe-blue"></div>
  </section>

</main>
</body>
</html>
```